Online Rug Store needs Clearance Banner

Website is: Lanternfield Carpets and Home
You can access it at: www.lanternfieldcarpetsandhome.com and login (top right) with password: trazok

*** update: When creating banners for my site, you have permission to use images from www.velbora.com, but ONLY for this project. The images/artwork are copyright allowable for use on www.lanternfieldcarpetsandhome.com projects.***

We need a home page banner sized 1000 wide x 500 tall pixels to promote a "Clearance Sale" on rugs. The banner can state:

1. Clearance Sale
2. Now in progress
3. Save an extra 20% with coupon code 'Mint20'
4. Ends March 31st
5. Plus Free Shipping and 30 day returns.

We prefer a banner that appears hand-drawn and artistic, not commercially produced. It is OK to use a room scene image, rug images, or just a colored/textured background with text and no images. Your choice.

Flat graphics with no shadows and 3-D effect preferred.
Attached is are 3 logo options, as well as an example banner with handcrafted, artistic styling that we prefer.

Target Market(s)

This should be an eye-catching banner to showcase a very urgent promotion. Consider using colors of red, white, gold, and black to make a strong statement on the home page.

Industry/Entity Type

Home And Garden

Requirements
Must have
• Winner must provide Photoshop editable file format (.psd format) including layers that can be edited.
Nice to have
• Hand-drawn, stenciled, scribbled, artistic graphics and fonts is nice because we sell rugs that are made by hand.
Should not have
• little to no shadowing. Avoid computerized graphics.

```html
<!DOCTYPE html>
<html lang="en">
<head>
<meta charset="utf-8">
<title>Clearance Sale Banner</title>
<link rel="stylesheet" href="https://fonts.googleapis.com/css2?family=Delius&family=Marcellus&family=Alegreya+Sans:wght@700&display=swap">
<style>
  :root {
    --page-bg: #cfd1d3;
    --ink: #111111;
    --sale-red: #c4141c;
    --sale-blue: #1f7ab8;
    --sale-green: #2f8a2f;
    --sale-gold: #dba400;
    --progress-red: #b3121b;
    --code-blue: #1f77b4;
    --free-green: #1f7a2a;
    --ends-gold: #e0a800;
    --band: rgba(255, 255, 255, 0.72);
  }
  * { margin: 0; padding: 0; box-sizing: border-box; }
  html, body {
    width: 1200px;
    height: 688px;
    overflow: hidden;
    background: var(--page-bg);
  }
  .banner {
    position: absolute;
    left: 67px;
    top: 68px;
    width: 1083px;
    height: 542px;
    overflow: hidden;
  }
  .rug-scene {
    position: absolute;
    inset: 0;
    background: linear-gradient(125deg,
      #d7c9b1 0%, #e3e0da 22%, #ecebe8 50%, #e4e2dd 74%, #c9b48f 86%, #6e4a2c 100%);
  }
  .headline {
    position: absolute;
    top: 26px;
    left: 0;
    width: 100%;
    text-align: center;
    font-family: "Delius", "Comic Sans MS", cursive;
    font-size: 128px;
    line-height: 1;
    color: var(--ink);
    letter-spacing: 1px;
  }
  .headline .s { color: var(--sale-red); }
  .headline .a { color: var(--sale-blue); }
  .headline .l { color: var(--sale-green); }
  .headline .e { color: var(--sale-gold); }
  .status {
    position: absolute;
    top: 172px;
    left: 0;
    width: 100%;
    text-align: center;
    font-family: "Alegreya Sans", "Optima", sans-serif;
    font-weight: 700;
    font-size: 46px;
    color: var(--progress-red);
  }
  .offer {
    position: absolute;
    top: 282px;
    left: 0;
    width: 100%;
    text-align: center;
    font-family: "Alegreya Sans", "Optima", sans-serif;
    font-weight: 700;
    font-size: 35px;
    color: var(--ink);
  }
  .offer .code { color: var(--code-blue); }
  .perk-band {
    position: absolute;
    top: 421px;
    height: 57px;
    background: var(--band);
  }
  .perk-band.left { left: 0; width: 507px; clip-path: polygon(0 0, 100% 0, 96% 100%, 0 100%); }
  .perk-band.right { left: 500px; width: 415px; clip-path: polygon(5% 0, 100% 0, 100% 100%, 0 100%); }
  .perk {
    position: absolute;
    top: 427px;
    font-family: "Marcellus", "Optima", sans-serif;
    font-size: 36px;
    line-height: 44px;
    color: var(--ink);
    text-align: center;
    transform: translateX(-50%);
    white-space: nowrap;
  }
  .perk.shipping { left: 234px; }
  .perk.returns { left: 745px; }
  .perk .accent { color: var(--free-green); font-family: "Alegreya Sans", sans-serif; font-weight: 700; }
  .deadline {
    position: absolute;
    left: 1000px;
    top: 432px;
    width: 150px;
    transform: translateX(-50%);
    text-align: center;
    font-family: "Alegreya Sans", "Optima", sans-serif;
    font-weight: 700;
    font-size: 23px;
    line-height: 46px;
    color: var(--ends-gold);
  }
  .deadline .label { display: block; padding-left: 30px; }
  .deadline sup { font-size: 13px; }
</style>
</head>
<body>
  <section class="banner">
    <div class="rug-scene" role="img" aria-label="Photograph of a white carved trellis-pattern rug lying diagonally over a beige rug and wooden floor"></div>
    <h1 class="headline">Clearance <span class="s">S</span><span class="a">a</span><span class="l">l</span><span class="e">e</span></h1>
    <p class="status">Now in progress</p>
    <p class="offer">Save an extra 20% with coupon code <span class="code">Mint 20</span></p>
    <div class="perk-band left"></div>
    <div class="perk-band right"></div>
    <p class="perk shipping"><span class="accent">FREE</span> SHIPPING</p>
    <p class="perk returns"><span class="accent">30</span> DAY RETURNS</p>
    <p class="deadline"><span class="label">Ends</span>March 31<sup>st</sup></p>
  </section>
</body>
</html>
```